New Company Letterhead

Hi All

We are looking for a fresh new letterhead. At present we have rolling colour behind our logo but would like one flat colour. See attached for examples of our current letterhead, logos and company colour chart. All information currently contained within the letterhead (i.e. address, ABN, tel, fax, email etc) needs to still be included in the new letterhead. Preferred font is Helvetica or something similar.

Any queries please shout.

Many thanks & best of luck,

Rosalind Pemberton
Marbury Estate Agents

Hi Designers Great work so far! Would it be possible to add to your designs the phrase; Done. Different. Preferably in a light grey? Many thanks, Ros

Industry/Entity Type

It Company

```html
<!DOCTYPE html>
<html lang="en">
<head>
<meta charset="utf-8">
<title>Marbury Estate Agents – Letterhead</title>
<link rel="stylesheet" href="https://fonts.googleapis.com/css2?family=Source+Sans+3:wght@400;700&display=swap">
<style>
  :root {
    --backdrop: #3b3b3d;
    --paper: #ffffff;
    --brand-teal: #0b5a7a;
    --band: #0b5a7a;
    --ink: #1c1c1c;
    --tagline-grey: #b9bfc4;
  }
  * { margin: 0; padding: 0; box-sizing: border-box; }
  html, body {
    width: 1200px; height: 999px; overflow: hidden;
    background: var(--backdrop);
    font-family: "Source Sans 3", "Helvetica Neue", Arial, sans-serif;
  }
  .letterhead {
    position: absolute; left: 274px; top: 38px;
    width: 652px; height: 922px;
    background: var(--paper);
  }
  .brand {
    position: absolute; left: 18px; top: 31px;
    display: flex; align-items: center; gap: 8px;
  }
  .brand-square {
    width: 14px; height: 14px; background: var(--brand-teal);
  }
  .brand-name {
    font-size: 21px; font-weight: 400; color: var(--brand-teal);
    letter-spacing: 0.5px; line-height: 1;
  }
  .tagline {
    position: absolute; right: 28px; top: 36px;
    font-size: 15px; font-weight: 400; color: var(--tagline-grey);
    letter-spacing: 0.5px; line-height: 1;
  }
  .company-details {
    position: absolute; left: 19px; top: 834px;
    font-size: 11px; color: var(--ink); line-height: 14px;
  }
  .company-name {
    font-size: 13px; font-weight: 700; color: var(--brand-teal);
    line-height: 16px;
  }
  .company-abn { margin-bottom: 5px; }
  .contact-list {
    position: absolute; left: 401px; top: 842px;
    list-style: none; font-size: 11px; color: var(--ink);
  }
  .contact-list li {
    display: flex; align-items: center; gap: 6px; height: 13.5px;
  }
  .contact-icon { width: 12px; height: 10px; fill: var(--brand-teal); flex: none; }
  .footer-band {
    position: absolute; left: 0; bottom: 0; width: 100%; height: 22px;
    background: var(--band);
  }
</style>
</head>
<body>
  <main class="letterhead">
    <header class="brand">
      <span class="brand-square"></span>
      <span class="brand-name">Marbury Estate Agents</span>
    </header>

    <p class="tagline">Done. Different.</p>

    <section class="company-details">
      <p class="company-name">Marbury Estate Agents</p>
      <p class="company-abn">ABN: 48 517 203 966</p>
      <p>58 Harbour Street,</p>
      <p>Ettalong NSW 2257</p>
    </section>

    <ul class="contact-list">
      <li>
        <svg class="contact-icon" viewBox="0 0 12 10"><path d="M3 0h2l1 2-1.5 1c.6 1.6 1.8 2.8 3.4 3.4L9 5l2 1v2c0 1-1 2-2 2C5 10 1.5 6.5 1.5 2 1.5 1 2 0 3 0z"/></svg>
        (02) 4810 5522
      </li>
      <li>
        <svg class="contact-icon" viewBox="0 0 12 10"><rect x="3" y="0" width="6" height="3"/><rect x="1" y="3.5" width="10" height="4" rx="1"/><rect x="3" y="8" width="6" height="2"/></svg>
        (02) 4810 5523
      </li>
      <li>
        <svg class="contact-icon" viewBox="0 0 12 10"><rect x="0" y="1.5" width="12" height="7" rx="1"/></svg>
        office@marburyestateagents.com.au
      </li>
      <li>
        <svg class="contact-icon" viewBox="0 0 12 10"><path d="M11 0 1 5l4 1 1 4z"/></svg>
        www.marburyestateagents.com.au
      </li>
    </ul>

    <div class="footer-band"></div>
  </main>
</body>
</html>
```